Flyer-Design für renomiertes Kosmetikstudio
Zielgruppe
Renomiertes Kosmetikstudio sucht hochwertiges Design für neue Flyer.
Zielgruppe Männer + Frauen die auf ihr Äußeres viel Wert legen.
Aufgabenstellung
Geradliniges Desgin unter Berücksichtigung von ganzheitlichen Farben (chakren). Edel.
Wir hätten gerne ein Angebot für Männer als auch für Frauen. Evtl. Aufteilung in 2 getrennte Flyer oder Flyer auf einer Seite Männer und umgedreht auf der anderen Seite für Frauen.?
Behandlungsbereiche die aufgenommen werden müssten:
Frauen
- Wimpernverlängerung
- Wimpernlifting
- Kosmetikbehandlung (Fresh Start - Deep Glow Konzept) ausführlicher text dazu
zzgl. möglichen Bausteinen
- Fußpflege
- Nageldesign
- Enthaarung mit Zuckerpaste
- Massagen
Männer:
- Kosmetikbehandlung
- Maniküre
-- Massage
- Enthaarung
Für die Kosmetik hätte ich gerne jeweils 1 Seite komplett um hier mehr Infos rein zu packen zur FRESH START Behandlung.
Platz für Preise der Behandlungen und bausteine.
Gewünscht Din Lang Format, gerne aber auch offen für neue Ideen.

```html
<!DOCTYPE html>
<html lang="de">
<head>
<meta charset="utf-8">
<title>Velluto – Preisliste 2019</title>
<link rel="stylesheet" href="https://fonts.googleapis.com/css2?family=Ubuntu:ital,wght@0,400;0,500;0,700;1,700&display=swap">
<style>
:root{
  --pink:#d86aa9;
  --pink-deep:#c2418f;
  --pink-soft:#ec9ac7;
  --grey:#8d8d8d;
  --grey-dark:#5c5c5c;
  --grey-light:#f1f1f1;
  --line:#cfcfcf;
  --paper:#ffffff;
  --backdrop:#e8e8e8;
  --photo-warm:#d9c3a3;
  --photo-skin:#e6d2c4;
}
*{box-sizing:border-box;margin:0;padding:0}
html,body{width:1200px;height:2400px;overflow:hidden}
body{background:var(--backdrop);font-family:"Ubuntu",sans-serif;color:var(--grey-dark)}
.spread{position:absolute;left:30px;width:1140px;height:806px;display:flex;background:var(--paper);box-shadow:0 12px 40px rgba(0,0,0,.12)}
.spread--outside{top:250px}
.spread--inside{top:1340px}
.panel{position:relative;width:380px;height:806px;overflow:hidden;background:var(--paper)}
.panel + .panel{border-left:1px solid #ececec}
.top-rule{position:absolute;top:0;left:0;right:0;height:8px;background:var(--pink)}
.photo{position:absolute;left:0;right:0}
.wave{position:absolute;left:0;width:100%;display:block}
.section-title{font-weight:700;font-style:italic;color:var(--pink-deep);font-size:19px;margin-bottom:4px}
.section-intro{font-size:9.5px;line-height:1.45;color:var(--grey);margin-bottom:18px}
.content{position:absolute;left:26px;right:26px}
.price-box{position:relative;border:1.5px solid var(--line);border-radius:10px;padding:14px 8px 8px;margin-bottom:26px}
.price-box__label{position:absolute;top:-10px;left:50%;transform:translateX(-50%);background:var(--pink-soft);color:#fff;font-size:10.5px;padding:3px 16px;border-radius:10px;white-space:nowrap}
.price-row{display:grid;grid-template-columns:1fr 62px 62px;align-items:center;height:17px;font-size:9.5px;color:var(--grey-dark)}
.price-row:nth-child(odd){background:var(--grey-light)}
.price-row span{white-space:nowrap;overflow:hidden}
.price-row .val{display:flex;align-items:center;gap:5px;justify-content:flex-end;padding-right:4px;border-left:1px solid var(--line)}
.icon-dot{width:8px;height:8px;border:1.3px solid var(--pink);border-radius:50%;flex:none}
.body-text{font-size:9.5px;line-height:1.5;color:var(--grey);margin-bottom:10px}
.pill{display:inline-block;background:var(--pink);color:#fff;border-radius:14px;font-size:13px;padding:4px 16px;letter-spacing:.3px}
.brand{font-family:"Ubuntu",sans-serif;font-weight:500;letter-spacing:.5px;font-size:26px}
.tagline{font-size:10px;letter-spacing:.3px}
.booking-box{position:absolute;background:var(--pink-deep);border:2px solid #fff;outline:3px solid var(--pink-deep);color:#fff;text-align:center}
/* cover */
.cover__logo{position:absolute;top:34px;left:0;right:0;text-align:center;color:var(--grey-dark)}
.cover__logo .tagline{color:var(--grey);margin-top:2px}
.cover__title{position:absolute;top:612px;left:0;right:0;text-align:center;color:#fff;font-size:40px;letter-spacing:5px;font-weight:400}
.cover__year{position:absolute;top:668px;left:40px;right:40px;display:flex;align-items:center;gap:12px;color:#fff;font-size:13px}
.cover__year::before,.cover__year::after{content:"";flex:1;height:1.5px;background:#fff}
.cover__url{position:absolute;top:718px;left:0;right:0;text-align:center}
/* contact panel */
.contact__welcome{position:absolute;top:16px;left:0;right:0;text-align:center}
.contact__welcome .pill{font-size:11px;padding:3px 14px}
.contact__team{position:absolute;top:66px;left:200px;width:140px;height:110px;border:4px solid var(--pink);border-radius:12px;background:linear-gradient(160deg,#6b5a55,#2f2a2a)}
.contact__body{position:absolute;top:230px;left:22px;right:22px;color:#fff;display:grid;grid-template-columns:1fr 1fr;gap:14px}
.contact__logo{grid-column:1/3;color:#fff}
.contact__logo .brand{font-size:22px}
.contact__head{font-size:10px;font-weight:500;margin-bottom:8px}
.contact__text{font-size:8.5px;line-height:1.55}
.hours{display:grid;grid-template-columns:56px 1fr;font-size:8.5px;line-height:1.5}
.social{display:flex;gap:10px;margin-top:16px}
.social span{width:22px;height:22px;border:2px solid #fff;border-radius:4px}
.contact__url{position:absolute;bottom:22px;left:0;right:0;text-align:center}
.contact__url .pill{font-size:13px}
</style>
</head>
<body>

<section class="spread spread--outside">

  <article class="panel panel--feet-nails">
    <div class="top-rule"></div>
    <div class="content" style="top:36px">
      <h2 class="section-title">Fußpflege</h2>
      <p class="section-intro">Klassische Fußpflege mit Fußbad, auf Wunsch gerne auch mit Lack oder dauerhaftem Nagellack. Zubuchbar: Fußmassage, Fußmaske etc.</p>
      <div class="price-box">
        <div class="price-box__label">Fußpflege</div>
        <div class="price-row"><span>Klassische Fußpflege inkl. Fußbad</span><span class="val"><i class="icon-dot"></i>40 min.</span><span class="val"><i class="icon-dot"></i>38,00</span></div>
        <div class="price-row"><span>Fußpflege mit dauerhaftem Lack</span><span class="val"><i class="icon-dot"></i>75 min.</span><span class="val"><i class="icon-dot"></i>53,00</span></div>
        <div class="price-row"><span>Zubuchbar: Klarlack</span><span class="val"><i class="icon-dot"></i>5 min.</span><span class="val"><i class="icon-dot"></i>5,00</span></div>
        <div class="price-row"><span>Zubuchbar: Farblack</span><span class="val"><i class="icon-dot"></i>10 min.</span><span class="val"><i class="icon-dot"></i>10,00</span></div>
        <div class="price-row"><span>Fußpeeling</span><span class="val"><i class="icon-dot"></i>5 min.</span><span class="val"><i class="icon-dot"></i>5,00</span></div>
        <div class="price-row"><span>Kleine Fußmassage</span><span class="val"><i class="icon-dot"></i>10 min.</span><span class="val"><i class="icon-dot"></i>12,00</span></div>
        <div class="price-row"><span>Ablackieren</span><span class="val"><i class="icon-dot"></i>5 min.</span><span class="val"><i class="icon-dot"></i>4,00</span></div>
        <div class="price-row"><span>French</span><span class="val"></span><span class="val"><i class="icon-dot"></i>+ 5,00</span></div>
      </div>
      <h2 class="section-title">Nageldesign</h2>
      <p class="section-intro">Gepflegte Hände sind täglich unsere Visitenkarte. Von der klassischen Maniküre bis hin zur Nagelmodellage finden Sie garantiert die passende Behandlung.</p>
      <div class="price-box">
        <div class="price-box__label">Nageldesign</div>
        <div class="price-row"><span>Maniküre</span><span class="val"><i class="icon-dot"></i>20 min.</span><span class="val"><i class="icon-dot"></i>17,00</span></div>
        <div class="price-row"><span>Dauerhafter Nagellack</span><span class="val"><i class="icon-dot"></i>45 min.</span><span class="val"><i class="icon-dot"></i>29,00</span></div>
        <div class="price-row"><span>Gelmodellage mit neu Verlängerung</span><span class="val"><i class="icon-dot"></i>90 min.</span><span class="val"><i class="icon-dot"></i>64,50</span></div>
        <div class="price-row"><span>Gelmodellage auffüllen</span><span class="val"><i class="icon-dot"></i>75 min.</span><span class="val"><i class="icon-dot"></i>49,50</span></div>
        <div class="price-row"><span>Naturnagelverstärkung</span><span class="val"><i class="icon-dot"></i>60 min.</span><span class="val"><i class="icon-dot"></i>39,50</span></div>
        <div class="price-row"><span>Fresh up</span><span class="val"><i class="icon-dot"></i>45 min.</span><span class="val"><i class="icon-dot"></i>20,00</span></div>
        <div class="price-row"><span>Wellnessmaniküre</span><span class="val"><i class="icon-dot"></i>35 min.</span><span class="val"><i class="icon-dot"></i>35,00</span></div>
      </div>
    </div>
    <div class="photo" style="top:680px;height:126px;background:linear-gradient(135deg,#f4ece8,var(--photo-skin))" role="img" aria-label="Foto: Hände bei der Maniküre"></div>
    <svg class="wave" style="top:660px;height:50px" viewBox="0 0 380 50" preserveAspectRatio="none" aria-hidden="true">
      <path d="M0 0H380V18C300 2 240 40 160 30S40 10 0 34Z" fill="#fff"/>
      <path d="M0 34C40 10 90 22 160 30S300 2 380 18V24C300 10 240 44 160 36S40 18 0 40Z" fill="var(--pink-soft)"/>
    </svg>
  </article>

  <article class="panel panel--contact" style="background:var(--pink)">
    <div class="photo" style="top:0;height:230px;background:linear-gradient(160deg,#f3ead9,var(--photo-warm))" role="img" aria-label="Foto: Empfangsbereich des Studios"></div>
    <div class="contact__welcome"><span class="pill">Wir freuen uns auf Ihren Besuch!</span></div>
    <div class="contact__team" role="img" aria-label="Foto: das Team des Studios"></div>
    <svg class="wave" style="top:180px;height:60px" viewBox="0 0 380 60" preserveAspectRatio="none" aria-hidden="true">
      <path d="M0 30C80 0 160 50 240 30S340 10 380 20V60H0Z" fill="var(--pink)"/>
    </svg>
    <div class="contact__body">
      <div class="contact__logo"><div class="brand">Velluto</div><div class="tagline">Kosmetikstudio</div></div>
      <div>
        <div class="contact__head">Kontakt</div>
        <p class="contact__text">Lindenweg 14<br>86150 Musterau</p>
        <p class="contact__text" style="margin-top:12px">
          <svg width="9" height="9" viewBox="0 0 24 24" aria-hidden="true"><path fill="#fff" d="M6.6 10.8a15 15 0 0 0 6.6 6.6l2.2-2.2c.3-.3.7-.4 1-.2 1.1.4 2.3.6 3.6.6.6 0 1 .4 1 1V20c0 .6-.4 1-1 1A17 17 0 0 1 3 4c0-.6.4-1 1-1h3.5c.6 0 1 .4 1 1 0 1.3.2 2.5.6 3.6.1.3 0 .7-.2 1z"/></svg>
          0831 55 20 418<br>✉ info@velluto-studio.de<br>◦ velluto.pflegeshop.de</p>
        <div class="social" aria-hidden="true"><span></span><span></span><span></span></div>
      </div>
      <div>
        <div class="contact__head">Öffnungszeiten</div>
        <div class="hours"><span>Mo, Di:</span><span>9:00 – 18:00 Uhr</span><span>Mi, Do:</span><span>9:00 – 19:30 Uhr</span><span>Freitag:</span><span>9:00 – 16:00 Uhr</span></div>
        <p class="contact__text" style="margin-top:10px">Samstag und Abendtermine<br>nach Vereinbarung</p>
      </div>
    </div>
    <div class="booking-box" style="left:210px;top:440px;width:130px;height:100px;padding-top:14px">
      <svg width="20" height="20" viewBox="0 0 24 24" aria-hidden="true"><rect x="3" y="5" width="18" height="16" rx="2" fill="none" stroke="#fff" stroke-width="2"/><path d="M3 10h18M8 3v4M16 3v4M9 15l2 2 4-4" fill="none" stroke="#fff" stroke-width="2"/></svg>
      <div style="font-size:12px;letter-spacing:3px;line-height:1.3;margin-top:4px">TERMINE<br>ONLINE<br>BUCHEN!</div>
    </div>
    <div class="photo" style="top:590px;height:216px;background:linear-gradient(160deg,#f5efe4,var(--photo-warm))" role="img" aria-label="Foto: Behandlungsraum des Studios"></div>
    <svg class="wave" style="top:570px;height:50px" viewBox="0 0 380 50" preserveAspectRatio="none" aria-hidden="true">
      <path d="M0 0H380V20C300 40 220 10 150 26S40 40 0 30Z" fill="var(--pink)"/>
      <path d="M0 30C40 40 90 34 150 26S300 40 380 20V26C300 46 220 18 150 32S40 46 0 36Z" fill="var(--grey)"/>
    </svg>
    <div class="contact__url"><span class="pill">www.velluto-studio.de</span></div>
  </article>

  <article class="panel panel--cover" style="background:linear-gradient(#f7f7f7,#e6e6e6)">
    <div class="cover__logo"><div class="brand">Velluto</div><div class="tagline">Kosmetikstudio</div></div>
    <div class="photo" style="top:120px;height:460px;background:linear-gradient(150deg,#ececec,var(--photo-skin) 60%,#d8c1b3)" role="img" aria-label="Foto: lächelnde Frau bei der Gesichtspflege"></div>
    <svg class="wave" style="top:100px;height:40px" viewBox="0 0 380 40" preserveAspectRatio="none" aria-hidden="true">
      <path d="M0 0H380V20C300 5 220 30 150 18S50 10 0 24Z" fill="#f3f3f3"/>
      <path d="M0 24C50 10 90 8 150 18S300 5 380 20V26C300 12 220 36 150 24S50 16 0 30Z" fill="var(--grey)"/>
    </svg>
    <svg class="wave" style="top:530px;height:60px" viewBox="0 0 380 60" preserveAspectRatio="none" aria-hidden="true">
      <path d="M0 30C80 10 150 40 230 24S340 10 380 16V60H0Z" fill="var(--grey)"/>
      <path d="M0 38C80 18 150 48 230 32S340 18 380 24V60H0Z" fill="var(--pink)"/>
    </svg>
    <div style="position:absolute;top:588px;left:0;right:0;bottom:0;background:var(--pink)"></div>
    <div class="booking-box" style="left:214px;top:440px;width:130px;height:118px;padding-top:14px">
      <svg width="18" height="18" viewBox="0 0 24 24" aria-hidden="true"><path fill="#fff" d="M6.6 10.8a15 15 0 0 0 6.6 6.6l2.2-2.2c.3-.3.7-.4 1-.2 1.1.4 2.3.6 3.6.6.6 0 1 .4 1 1V20c0 .6-.4 1-1 1A17 17 0 0 1 3 4c0-.6.4-1 1-1h3.5c.6 0 1 .4 1 1 0 1.3.2 2.5.6 3.6.1.3 0 .7-.2 1z"/></svg>
      <div style="font-size:11px;letter-spacing:3px;margin-top:2px">TERMINE:</div>
      <div style="font-size:19px;line-height:1.1">0831<br>55 20 418</div>
    </div>
    <h1 class="cover__title">PREISLISTE</h1>
    <div class="cover__year">für 2019</div>
    <div class="cover__url"><span class="pill" style="background:var(--pink-deep)">www.velluto-studio.de</span></div>
  </article>
</section>

<section class="spread spread--inside">

  <article class="panel panel--lashes">
    <div class="top-rule"></div>
    <div class="content" style="top:36px">
      <h2 class="section-title">Wimpernverlängerung</h2>
      <p class="section-intro">Mit einer professionellen Wimpernverlängerung oder Wimpernverdichtung genießen Sie jeden Morgen einen natürlich wachen Blick.</p>
      <div class="price-box">
        <div class="price-box__label">Wimpernverlängerung</div>
        <div class="price-row"><span>Neuansatz</span><span class="val"><i class="icon-dot"></i>90 min.</span><span class="val"><i class="icon-dot"></i>160,00</span></div>
        <div class="price-row"><span>Neuansatz Volumentechnik</span><span class="val"><i class="icon-dot"></i>90 min.</span><span class="val"><i class="icon-dot"></i>280,00</span></div>
        <div class="price-row"><span>Refill nach 1 Woche</span><span class="val"><i class="icon-dot"></i>40 min.</span><span class="val"><i class="icon-dot"></i>45,00</span></div>
        <div class="price-row"><span>Refill nach 2 Wochen</span><span class="val"><i class="icon-dot"></i>60 min.</span><span class="val"><i class="icon-dot"></i>52,00</span></div>
        <div class="price-row"><span>Refill nach 3 Wochen</span><span class="val"><i class="icon-dot"></i>60 min.</span><span class="val"><i class="icon-dot"></i>68,00</span></div>
        <div class="price-row"><span>Wimpernverlängerung entfernen</span><span class="val"><i class="icon-dot"></i>30 min.</span><span class="val"><i class="icon-dot"></i>25,00</span></div>
        <div class="price-row"><span>NEU: Aufpreis Volumentechnik</span><span class="val"><i class="icon-dot"></i>15 min.</span><span class="val"><i class="icon-dot"></i>+ 15,00</span></div>
      </div>
      <h2 class="section-title">Wimpernlifting</h2>
      <p class="section-intro">Mit einem professionellen Wimpernlifting erhalten Ihre eigenen Wimpern einen schönen, langanhaltenden Schwung.</p>
      <div class="price-box">
        <div class="price-box__label">Wimpernlifting</div>
        <div class="price-row"><span>Neuansatz</span><span class="val"><i class="icon-dot"></i>90 min.</span><span class="val"><i class="icon-dot"></i>190,00</span></div>
        <div class="price-row"><span>Neuansatz Volumentechnik</span><span class="val"><i class="icon-dot"></i>90 min.</span><span class="val"><i class="icon-dot"></i>280,00</span></div>
        <div class="price-row"><span>Refill nach 2 Wochen</span><span class="val"><i class="icon-dot"></i>45 min.</span><span class="val"><i class="icon-dot"></i>45,00</span></div>
      </div>
    </div>
    <div class="photo" style="top:560px;height:246px;background:linear-gradient(150deg,#f3ede9,var(--photo-skin) 70%,#c9d6e6)" role="img" aria-label="Foto: Augenpartie mit langen Wimpern"></div>
    <svg class="wave" style="top:540px;height:60px" viewBox="0 0 380 60" preserveAspectRatio="none" aria-hidden="true">
      <path d="M0 0H380V30C300 50 230 10 160 26S50 40 0 20Z" fill="#fff"/>
      <path d="M0 20C50 40 100 34 160 26S300 50 380 30V38C300 58 230 18 160 34S50 48 0 28Z" fill="var(--pink-soft)"/>
    </svg>
  </article>

  <article class="panel panel--cosmetics">
    <div class="photo" style="top:0;height:240px;background:linear-gradient(160deg,#f4f2ef,#cfc8c2)" role="img" aria-label="Foto: Behandlungsliege im Kosmetikraum"></div>
    <svg class="wave" style="top:200px;height:60px" viewBox="0 0 380 60" preserveAspectRatio="none" aria-hidden="true">
      <path d="M0 34C70 10 150 44 230 30S340 14 380 22V26C340 18 250 36 230 36S70 16 0 40Z" fill="var(--pink-soft)"/>
      <path d="M0 40C70 16 150 50 230 36S340 20 380 26V60H0Z" fill="#fff"/>
    </svg>
    <div class="content" style="top:262px">
      <h2 class="section-title" style="text-align:center">Kosmetikbehandlungen</h2>
      <div style="text-align:center;margin:2px 0 12px"><span class="pill" style="font-size:10.5px;font-style:italic;background:var(--pink-soft)">Fresh Start - Deep Glow Konzept</span></div>
      <p class="body-text">Beim ersten Termin analysieren wir Ihren Hauttyp in Ruhe und stimmen Reinigung, Peeling und Pflege genau auf Ihre Bedürfnisse ab. So entsteht ein Plan, der wirklich zu Ihnen passt.</p>
      <p class="body-text">Der Deep Glow Termin baut darauf auf: Wirkstoffe dringen tiefer ein, die Haut wird sichtbar praller und strahlender. Regelmäßige Folgebehandlungen festigen das Ergebnis und halten Ihr Hautbild dauerhaft im Gleichgewicht. Auf Wunsch ergänzen wir Massage, Maske oder Augenpflege als Baustein.</p>
      <p class="body-text">Für Damen wie Herren gleichermaßen geeignet – wir beraten Sie gern persönlich zu Ablauf, Dauer und passenden Pflegeprodukten für zu Hause.</p>
      <div class="price-box" style="margin-top:22px">
        <div class="price-box__label" style="font-style:italic">Fresh Start - Deep Glow</div>
        <div class="price-row"><span>Fresh Start Analyse</span><span class="val"><i class="icon-dot"></i>90 min.</span><span class="val"><i class="icon-dot"></i>190,00</span></div>
        <div class="price-row"><span>Deep Glow Intensiv</span><span class="val"><i class="icon-dot"></i>90 min.</span><span class="val"><i class="icon-dot"></i>280,00</span></div>
        <div class="price-row"><span>Folgebehandlung</span><span class="val"><i class="icon-dot"></i>45 min.</span><span class="val"><i class="icon-dot"></i>45,00</span></div>
      </div>
      <p class="body-text">Alle Bausteine lassen sich frei kombinieren. Sprechen Sie uns an, gemeinsam finden wir die ideale Zusammenstellung für Ihre Haut.</p>
    </div>
  </article>

  <article class="panel panel--waxing-massage">
    <div class="top-rule"></div>
    <div class="content" style="top:36px">
      <h2 class="section-title">Enthaarung mit Zuckerpaste</h2>
      <p class="section-intro">Sanfte Haarentfernung mit natürlicher Zuckerpaste – besonders hautschonend und lange glatt, für Damen und Herren gleichermaßen geeignet.</p>
      <div class="price-box">
        <div class="price-box__label">Enthaarung</div>
        <div class="price-row"><span>Beratungsgespräch Sugaring + Pflege</span><span class="val"></span><span class="val"><i class="icon-dot"></i>25,00</span></div>
        <div class="price-row"><span>Unterschenkel inkl. Knie</span><span class="val"><i class="icon-dot"></i>32,00</span><span class="val"><i class="icon-dot"></i>49,00</span></div>
        <div class="price-row"><span>Beine komplett</span><span class="val"><i class="icon-dot"></i>68,00</span><span class="val"><i class="icon-dot"></i>95,00</span></div>
        <div class="price-row"><span>Arme komplett</span><span class="val"><i class="icon-dot"></i>30,00</span><span class="val"><i class="icon-dot"></i>45,00</span></div>
        <div class="price-row"><span>Achseln</span><span class="val"><i class="icon-dot"></i>24,00</span><span class="val"><i class="icon-dot"></i>34,00</span></div>
        <div class="price-row"><span>Teile Gesicht</span><span class="val"><i class="icon-dot"></i>10,00</span><span class="val"><i class="icon-dot"></i>15,00</span></div>
        <div class="price-row"><span>Bikinizone</span><span class="val"><i class="icon-dot"></i>32,00</span><span class="val"><i class="icon-dot"></i>42,00</span></div>
        <div class="price-row"><span>Nasen- und Ohrenhaare</span><span class="val"><i class="icon-dot"></i>10,00</span><span class="val"></span></div>
        <div class="price-row"><span>Intim (nur für Damen)</span><span class="val"></span><span class="val"><i class="icon-dot"></i>68,00</span></div>
        <div class="price-row"><span>Rücken</span><span class="val"><i class="icon-dot"></i>54,00</span><span class="val"><i class="icon-dot"></i>74,00</span></div>
        <div class="price-row"><span>Bauch</span><span class="val"><i class="icon-dot"></i>32,00</span><span class="val"><i class="icon-dot"></i>45,00</span></div>
        <div class="price-row"><span>Brust</span><span class="val"><i class="icon-dot"></i>32,00</span><span class="val"><i class="icon-dot"></i>45,00</span></div>
        <div class="price-row"><span>Oberlippe</span><span class="val"><i class="icon-dot"></i>10,00</span><span class="val"><i class="icon-dot"></i>14,00</span></div>
        <div class="price-row"><span>Schultern</span><span class="val"><i class="icon-dot"></i>32,00</span><span class="val"><i class="icon-dot"></i>45,00</span></div>
      </div>
      <h2 class="section-title">Massagen</h2>
      <p class="section-intro">Entspannung für Körper und Geist: Unsere Massagen lösen Verspannungen, fördern die Durchblutung und schenken Ihnen eine wohltuende Auszeit vom Alltag.</p>
      <div class="price-box">
        <div class="price-box__label">Massagen</div>
        <div class="price-row"><span>Beratungsgespräch Sugaring + Pflege</span><span class="val"><i class="icon-dot"></i>25,00</span><span class="val"><i class="icon-dot"></i>49,00</span></div>
        <div class="price-row"><span>Unterschenkel inkl. Knie</span><span class="val"><i class="icon-dot"></i>32,00</span><span class="val"><i class="icon-dot"></i>49,00</span></div>
        <div class="price-row"><span>Beine komplett</span><span class="val"><i class="icon-dot"></i>68,00</span><span class="val"><i class="icon-dot"></i>95,00</span></div>
        <div class="price-row"><span>Arme komplett</span><span class="val"><i class="icon-dot"></i>30,00</span><span class="val"><i class="icon-dot"></i>45,00</span></div>
        <div class="price-row"><span>Achseln</span><span class="val"><i class="icon-dot"></i>24,00</span><span class="val"><i class="icon-dot"></i>34,00</span></div>
        <div class="price-row"><span>Teile Gesicht</span><span class="val"><i class="icon-dot"></i>10,00</span><span class="val"><i class="icon-dot"></i>15,00</span></div>
      </div>
    </div>
  </article>
</section>

</body>
</html>
```